Photo Storage Service - Web Application

This is web design for a simple photo storage service.
There is a web page and on the left side is a list of folders and on the right side there are photo thumbnails. By pressing a photo thumbnail, they will see the full size (it's just a link to a different page).
This project is limited only to ONE page, which is the page with the folders list and the thumbnails. However it contains some features that I will try to list here:
- Name of the service: Tavo Vault
- Location of account: http://username.tavo.example
- Folder list: Show all folders belonging to the user. Because you have to be able to drag photos to a folder, they have to be visible and cannot be hidden behind a menu item etc.
- Thumbnails with photos (in the future also videos)
- Adjusted view with smaller thumbnails and less space for folder list (so it is possible to view a larger quantity of thumbnails)- Select multiple thumbnails with rectangle- Show that a thumbnail is selected (maybe bold border?)
- Simple mobile view, but no emphasis on the mobile view in this design project.
- Drag one or more selected photos to a folder
- Delete one or more selected photos
- Drag a folder to another folder
- Rename folder
- Delete folder
- Create folder
- Show progress when deleting/moving (because it calls for every photo, so if there are 100 photos, it will delete 1 by 1 and it will take about 10 seconds - you could show progress bar or equivalent)
Background information: This is for a photo storage service NOT intended for sharing photos, but intended to indefinitely store photos and for yourself to browse your own photos.
It is a design requirement that it loads extremely fast. So we need to limit as much as possible extra graphics that cannot be done by CSS and other external libraries.
(I know this is ONLY design and nothing to do with CSS or libraries, but I can assess from the design if it might be heavy to load when implemented)
I have attached a crude screenshot of the current design, just for your understanding. It should not match this design and you are not in any way supposed to FIT your design into this same style or structure.
Target Market(s)
Consumers
Number of Pages Required
1 page
Font styles to use
Look and feel
Each slider illustrates characteristics of the customer's brand and the style your logo design should communicate.

```html
<!DOCTYPE html>
<html lang="en">
<head>
<meta charset="utf-8">
<title>Tavo Vault — My Image Gallery</title>
<link href="https://fonts.googleapis.com/css2?family=Roboto:wght@400;500;700;900&display=swap" rel="stylesheet">
<style>
  :root {
    --bg: #1c1d1f;
    --panel: #1c1d1f;
    --line: #38393c;
    --brand: #6cb800;
    --brand-dim: #3f6b0f;
    --text: #e6e6e6;
    --muted: #9a9b9e;
    --button-border: #47484c;
    --toggle-on: #36373a;
    --selected: #3a3b3e;
    --folder: #f3c53f;
    --thumb-frame: #e7eced;
    --thumb-sky: #414a5e;
    --thumb-sun: #f2cb4c;
    --thumb-hill: #2ab38b;
    --thumb-hill-dark: #1d9474;
  }
  * { box-sizing: border-box; margin: 0; padding: 0; }
  html, body { width: 1200px; height: 900px; overflow: hidden; background: var(--bg); }
  body { font-family: "Roboto", Arial, sans-serif; color: var(--text); position: relative; }

  .app-header { height: 48px; background: var(--brand); display: flex; align-items: center; padding-left: 22px; }
  .brand-name { font-weight: 900; font-size: 22px; letter-spacing: 1.5px; color: #fff; }

  .breadcrumb-bar { position: absolute; top: 62px; left: 22px; right: 22px; height: 40px; display: flex; align-items: center; }
  .back-button { width: 40px; height: 40px; background: var(--toggle-on); display: flex; align-items: center; justify-content: center; }
  .crumbs { display: flex; align-items: center; margin-left: 28px; font-size: 16px; gap: 10px; }
  .crumbs .sep { margin: 0 4px; }
  .sort-control { position: absolute; right: 40px; top: 0; width: 199px; height: 40px; border: 1px solid var(--line); display: flex; align-items: center; justify-content: space-between; padding: 0 14px; font-size: 16px; background: #222326; }
  .page-range { position: absolute; right: 0; top: 0; width: 40px; height: 40px; border: 1px solid var(--line); display: flex; align-items: center; justify-content: center; font-size: 11px; }

  .toolbar { position: absolute; top: 117px; left: 22px; right: 22px; height: 40px; }
  .toolbar > * { position: absolute; top: 0; height: 40px; }
  .btn { display: flex; align-items: center; justify-content: center; gap: 8px; font-size: 14px; font-weight: 700; letter-spacing: 1px; text-transform: uppercase; }
  .btn-create { left: 0; width: 140px; background: var(--brand-dim); color: #8aa066; }
  .btn-upload { left: 151px; width: 145px; background: var(--brand); color: #fff; }
  .btn-settings { left: 305px; width: 158px; border: 1px solid var(--button-border); color: #d8d8d8; }
  .action-group { left: 491px; width: 156px; display: flex; border: 1px solid var(--line); }
  .action-group span { flex: 1; display: flex; align-items: center; justify-content: center; border-right: 1px solid var(--line); }
  .action-group span:last-child { border-right: 0; }
  .btn-select-all { left: 675px; width: 172px; border: 1px solid var(--button-border); color: #d8d8d8; }
  .item-count { left: 878px; line-height: 40px; font-size: 15px; letter-spacing: .5px; }
  .toggle { display: flex; border: 1px solid var(--line); width: 79px; }
  .toggle span { flex: 1; display: flex; align-items: center; justify-content: center; }
  .toggle .on { background: var(--toggle-on); }
  .toggle-layout { left: 970px; }
  .toggle-size { left: 1077px; }

  .divider { position: absolute; top: 166px; left: 0; right: 0; height: 1px; background: var(--line); }

  .folder-list { position: absolute; top: 167px; left: 0; width: 302px; bottom: 0; border-right: 1px solid var(--line); padding: 14px 22px; list-style: none; }
  .folder-item { display: flex; align-items: center; height: 42px; font-size: 16px; letter-spacing: .3px; }
  .folder-item.account { gap: 14px; }
  .folder-item.child { padding-left: 20px; gap: 14px; }
  .folder-item.current { background: var(--selected); border: 1px solid #4a4b4f; padding-left: 16px; gap: 16px; margin-top: 0; }

  .thumb-grid { position: absolute; top: 189px; left: 340px; display: grid; grid-template-columns: repeat(6, 90px); grid-auto-rows: 94px; column-gap: 10px; row-gap: 21px; }
  .thumb { display: block; width: 90px; height: 94px; }
</style>
</head>
<body>
<svg width="0" height="0" style="position:absolute">
  <defs>
    <symbol id="photo-placeholder" viewBox="0 0 80 84">
      <rect width="80" height="84" fill="var(--thumb-frame)"/>
      <rect x="3.5" y="3.5" width="73" height="63" fill="var(--thumb-sky)"/>
      <circle cx="20" cy="21" r="6.5" fill="var(--thumb-sun)"/>
      <polygon points="40,54 56,33 76.5,53 76.5,66.5 40,66.5" fill="var(--thumb-hill-dark)"/>
      <polygon points="3.5,66.5 3.5,62 30,40 56,66.5" fill="var(--thumb-hill)"/>
    </symbol>
  </defs>
</svg>

<header class="app-header"><span class="brand-name">TAVOVAULT</span></header>

<nav class="breadcrumb-bar">
  <span class="back-button"><svg width="12" height="16" viewBox="0 0 12 16"><path d="M8 2 2 8l6 6" stroke="#ddd" stroke-width="1.6" fill="none"/></svg></span>
  <div class="crumbs">
    <svg width="12" height="15" viewBox="0 0 12 15"><circle cx="6" cy="4" r="3.5" fill="#eee"/><path d="M0 15c0-5 2.5-6.5 6-6.5S12 10 12 15z" fill="#eee"/></svg>
    <span>Username</span><span class="sep">&gt;</span>
    <svg width="28" height="24" viewBox="0 0 28 24"><rect x="1" y="1" width="26" height="22" fill="#1c1d1f" stroke="#fff" stroke-width="2"/><polygon points="4,20 12,10 17,16 20,13 24,20" fill="#fff"/><circle cx="20" cy="7" r="2" fill="#fff"/></svg>
    <span>My Image Gallery</span>
  </div>
  <div class="sort-control"><span>Sort by Date Taken</span><svg width="10" height="6" viewBox="0 0 10 6"><path d="M1 1l4 4 4-4" stroke="#888" fill="none"/></svg></div>
  <div class="page-range">1-9</div>
</nav>

<div class="toolbar">
  <span class="btn btn-create">+ Create</span>
  <span class="btn btn-upload"><svg width="18" height="13" viewBox="0 0 18 13"><path d="M4 12a4 4 0 0 1-.5-8A5.5 5.5 0 0 1 14 4a4 4 0 0 1 0 8z" fill="#fff"/><path d="M9 5l-3 3h2v3h2V8h2z" fill="var(--brand)"/></svg>Upload</span>
  <span class="btn btn-settings"><svg width="14" height="14" viewBox="0 0 14 14"><circle cx="7" cy="7" r="5" fill="none" stroke="#ddd" stroke-width="3" stroke-dasharray="2 1.9"/><circle cx="7" cy="7" r="3.5" fill="none" stroke="#ddd" stroke-width="2"/></svg>Settings</span>
  <div class="action-group">
    <span><svg width="14" height="10" viewBox="0 0 14 10"><ellipse cx="7" cy="5" rx="6.5" ry="4.5" fill="#666"/><circle cx="7" cy="5" r="2" fill="#1c1d1f"/></svg></span>
    <span><svg width="13" height="13" viewBox="0 0 13 13"><path d="M1 12l6-6M8 1a3 3 0 0 0 4 4L10 3z" stroke="#777" stroke-width="2" fill="#777"/></svg></span>
    <span><svg width="12" height="13" viewBox="0 0 12 13"><path d="M6 1v7M3 5l3 3 3-3M1 12h10" stroke="#ddd" stroke-width="1.6" fill="none"/></svg></span>
    <span><svg width="11" height="13" viewBox="0 0 11 13"><rect x="0" y="1.5" width="11" height="1.5" fill="#ddd"/><rect x="4" y="0" width="3" height="1.5" fill="#ddd"/><path d="M1.5 4h8l-.7 9H2.2z" fill="#ddd"/></svg></span>
  </div>
  <span class="btn btn-select-all"><svg width="15" height="15" viewBox="0 0 15 15"><circle cx="7.5" cy="7.5" r="7" fill="#ddd"/><path d="M4 7.5l2.5 2.5L11 5" stroke="#1c1d1f" stroke-width="2" fill="none"/></svg>Select All</span>
  <span class="item-count">18 Items</span>
  <div class="toggle toggle-layout">
    <span class="on"><svg width="11" height="11"><rect width="11" height="11" fill="#ddd"/></svg></span>
    <span><svg width="12" height="11"><rect width="12" height="7" fill="#ddd"/><rect y="9" width="12" height="2" fill="#ddd"/></svg></span>
  </div>
  <div class="toggle toggle-size">
    <span class="on"><svg width="12" height="12" viewBox="0 0 12 12"><path d="M1 4V1h3M8 1h3v3M11 8v3H8M4 11H1V8" stroke="#ddd" fill="none"/><rect x="3.5" y="3.5" width="5" height="5" fill="#ddd"/></svg></span>
    <span><svg width="14" height="10" viewBox="0 0 14 10"><path d="M1 3V1h3M10 1h3v2M13 7v2h-3M4 9H1V7" stroke="#ddd" fill="none"/><rect x="3" y="3" width="8" height="4" fill="#ddd"/></svg></span>
  </div>
</div>

<div class="divider"></div>

<ul class="folder-list">
  <li class="folder-item account"><svg width="22" height="28" viewBox="0 0 22 28"><circle cx="11" cy="7" r="6.5" fill="#bdbdbd"/><path d="M0 28c0-11 4-14 11-14s11 3 11 14z" fill="#bdbdbd"/></svg>Username</li>
  <li class="folder-item child"><svg width="26" height="20" viewBox="0 0 26 20"><path d="M0 2h9l2 2h13v4H0z" fill="#d9a92c"/><path d="M0 6h26l-1 14H1z" fill="var(--folder)"/></svg>Folder 3</li>
  <li class="folder-item child"><svg width="26" height="20" viewBox="0 0 26 20"><path d="M0 2h9l2 2h13v4H0z" fill="#d9a92c"/><path d="M0 6h26l-1 14H1z" fill="var(--folder)"/></svg>Folder 4</li>
  <li class="folder-item current"><svg width="28" height="24" viewBox="0 0 28 24"><rect x="1" y="1" width="26" height="22" fill="none" stroke="#fff" stroke-width="2"/><polygon points="4,20 12,10 17,16 20,13 24,20" fill="#fff"/><circle cx="20" cy="7" r="2" fill="#fff"/></svg>My Image Gallery</li>
</ul>

<main class="thumb-grid">
  <a class="thumb" href="#"><svg width="90" height="94" role="img" aria-label="Photo thumbnail"><use href="#photo-placeholder"/></svg></a>
  <a class="thumb" href="#"><svg width="90" height="94" role="img" aria-label="Photo thumbnail"><use href="#photo-placeholder"/></svg></a>
  <a class="thumb" href="#"><svg width="90" height="94" role="img" aria-label="Photo thumbnail"><use href="#photo-placeholder"/></svg></a>
  <a class="thumb" href="#"><svg width="90" height="94" role="img" aria-label="Photo thumbnail"><use href="#photo-placeholder"/></svg></a>
  <a class="thumb" href="#"><svg width="90" height="94" role="img" aria-label="Photo thumbnail"><use href="#photo-placeholder"/></svg></a>
  <a class="thumb" href="#"><svg width="90" height="94" role="img" aria-label="Photo thumbnail"><use href="#photo-placeholder"/></svg></a>
  <a class="thumb" href="#"><svg width="90" height="94" role="img" aria-label="Photo thumbnail"><use href="#photo-placeholder"/></svg></a>
  <a class="thumb" href="#"><svg width="90" height="94" role="img" aria-label="Photo thumbnail"><use href="#photo-placeholder"/></svg></a>
  <a class="thumb" href="#"><svg width="90" height="94" role="img" aria-label="Photo thumbnail"><use href="#photo-placeholder"/></svg></a>
  <a class="thumb" href="#"><svg width="90" height="94" role="img" aria-label="Photo thumbnail"><use href="#photo-placeholder"/></svg></a>
  <a class="thumb" href="#"><svg width="90" height="94" role="img" aria-label="Photo thumbnail"><use href="#photo-placeholder"/></svg></a>
  <a class="thumb" href="#"><svg width="90" height="94" role="img" aria-label="Photo thumbnail"><use href="#photo-placeholder"/></svg></a>
  <a class="thumb" href="#"><svg width="90" height="94" role="img" aria-label="Photo thumbnail"><use href="#photo-placeholder"/></svg></a>
  <a class="thumb" href="#"><svg width="90" height="94" role="img" aria-label="Photo thumbnail"><use href="#photo-placeholder"/></svg></a>
  <a class="thumb" href="#"><svg width="90" height="94" role="img" aria-label="Photo thumbnail"><use href="#photo-placeholder"/></svg></a>
  <a class="thumb" href="#"><svg width="90" height="94" role="img" aria-label="Photo thumbnail"><use href="#photo-placeholder"/></svg></a>
  <a class="thumb" href="#"><svg width="90" height="94" role="img" aria-label="Photo thumbnail"><use href="#photo-placeholder"/></svg></a>
  <a class="thumb" href="#"><svg width="90" height="94" role="img" aria-label="Photo thumbnail"><use href="#photo-placeholder"/></svg></a>
</main>
</body>
</html>
```